Business Consultancy Business Card Design

Business Card design required for Business Analysis and Project Consultancy business based in Scotland.

Company Name - Brevick Advisory

Back - Company Logo

Front Details

Owen Brevick
07642 918 305
owen.brevick@brevickadvisory.com
http://www.brevickadvisory.com

Colours should match the logo colours but I am open to design ideas.

```html
<!DOCTYPE html>
<html lang="en">
<head>
<meta charset="utf-8">
<title>Brevick Advisory – Business Cards</title>
<link href="https://fonts.googleapis.com/css2?family=Questrial&display=swap" rel="stylesheet">
<style>
  :root {
    --brand-blue: #0f9ae0;
    --brand-green: #6cb33f;
    --text-grey: #555a5f;
    --rule-green: #9cc97a;
    --card-white: #ffffff;
    --backdrop: #dcdcdc;
  }
  * { margin: 0; padding: 0; box-sizing: border-box; }
  html, body {
    width: 1200px; height: 1200px; overflow: hidden;
    background: var(--backdrop);
    font-family: "Questrial", "Century Gothic", sans-serif;
  }
  .sheet {
    position: relative; width: 1200px; height: 1200px;
  }
  .card {
    position: absolute; top: 449px;
    width: 540px; height: 302px;
    background: var(--card-white);
    box-shadow: 0 4px 14px rgba(0,0,0,0.22);
    overflow: hidden;
  }
  .card--front { left: 45px; }
  .card--back { left: 615px; }

  /* Front */
  .side-band {
    position: absolute; left: 20px; top: 0; width: 57px; height: 100%;
    background: var(--brand-blue);
  }
  .side-band__top {
    position: absolute; left: 0; top: 0; width: 100%; height: 56px;
    background: var(--brand-green);
  }
  .band-dot {
    position: absolute; left: 18px; top: 59px;
    width: 60px; height: 60px; border-radius: 50%;
    background: var(--card-white);
  }
  .title-divider {
    position: absolute; left: 91px; top: 72px;
    width: 2px; height: 38px; background: var(--text-grey);
  }
  .company-name {
    position: absolute; left: 106px; top: 74px;
    font-size: 32px; line-height: 1; letter-spacing: 0.5px;
    color: var(--text-grey); text-transform: uppercase; white-space: nowrap;
  }
  .person-name {
    position: absolute; left: 88px; top: 136px;
    font-size: 22px; line-height: 1; color: var(--brand-blue);
  }
  .name-rule {
    position: absolute; left: 88px; top: 172px;
    width: 421px; height: 1px; background: var(--rule-green);
  }
  .contact-list { list-style: none; }
  .contact-item {
    position: absolute; left: 57px;
    display: flex; align-items: center; gap: 9px;
    font-size: 15px; line-height: 1; color: var(--text-grey); white-space: nowrap;
  }
  .contact-item:nth-child(1) { top: 206px; }
  .contact-item:nth-child(2) { top: 226px; }
  .contact-item:nth-child(3) { top: 246px; }
  .contact-icon { width: 14px; height: 14px; flex: none; }

  /* Back */
  .back-dot {
    position: absolute; left: 213px; top: 67px;
    width: 114px; height: 114px; border-radius: 50%;
    background: var(--brand-blue);
  }
  .back-name {
    position: absolute; left: 0; width: 100%; top: 202px;
    text-align: center; font-size: 32px; line-height: 1; letter-spacing: 0.5px;
    color: var(--text-grey); text-transform: uppercase;
  }
</style>
</head>
<body>
<main class="sheet">
  <section class="card card--front" aria-label="Business card front">
    <div class="side-band"><div class="side-band__top"></div></div>
    <div class="band-dot"></div>
    <div class="title-divider"></div>
    <h1 class="company-name">Brevick Advisory</h1>
    <p class="person-name">Owen Brevick</p>
    <div class="name-rule"></div>
    <ul class="contact-list">
      <li class="contact-item">
        <svg class="contact-icon" viewBox="0 0 14 14" aria-hidden="true">
          <rect width="14" height="14" rx="2" fill="#6cb33f"/>
          <path d="M4 3.2l1.6-.4 1 2.2-1 .8c.5 1 1.3 1.8 2.3 2.3l.8-1 2.2 1-.4 1.6c-3.3.2-6.7-3.2-6.5-6.5z" fill="#fff"/>
        </svg>
        <span>07642 918 305</span>
      </li>
      <li class="contact-item">
        <svg class="contact-icon" viewBox="0 0 14 14" aria-hidden="true">
          <rect width="14" height="14" rx="2" fill="#6cb33f"/>
          <circle cx="7" cy="7" r="1.8" fill="none" stroke="#fff" stroke-width="1.2"/>
          <path d="M8.8 7v.8c0 1.4 2 1.4 2 0V7a3.8 3.8 0 1 0-1.5 3" fill="none" stroke="#fff" stroke-width="1.2"/>
        </svg>
        <span>owen.brevick@brevickadvisory.com</span>
      </li>
      <li class="contact-item">
        <svg class="contact-icon" viewBox="0 0 14 14" aria-hidden="true">
          <rect width="14" height="14" rx="2" fill="#6cb33f"/>
          <circle cx="7" cy="7" r="4" fill="none" stroke="#fff" stroke-width="1"/>
          <ellipse cx="7" cy="7" rx="1.7" ry="4" fill="none" stroke="#fff" stroke-width="1"/>
          <path d="M3 7h8" stroke="#fff" stroke-width="1"/>
        </svg>
        <span>http://www.brevickadvisory.com</span>
      </li>
    </ul>
  </section>

  <section class="card card--back" aria-label="Business card back">
    <div class="back-dot"></div>
    <h2 class="back-name">Brevick Advisory</h2>
  </section>
</main>
</body>
</html>
```